Corvane Supplies Business Card

Professional business card that stand out to our potential customers. Front and back with clean modern design

Industry/Entity Type

Oil and gas

Contact Information for Business Card

Name, address, website , office phone and cell number

Requirements
Must have
• Editable files for each employee

```html
<!DOCTYPE html>
<html lang="en">
<head>
<meta charset="utf-8">
<title>Corvane Supplies Business Card</title>
<link rel="stylesheet" href="https://fonts.googleapis.com/css2?family=Anton&family=Work+Sans:wght@400;600;700&display=swap">
<style>
  :root {
    --stage: #adadad;
    --card-dark: #232323;
    --card-dark-edge: #1b1b1b;
    --card-light: #ffffff;
    --brand-red: #e42526;
    --brand-cyan: #12a8cb;
    --ink: #111111;
    --ink-soft: #555555;
    --decor-warm: #fdf1ec;
    --decor-cool: #eef6f9;
  }
  * { margin: 0; padding: 0; box-sizing: border-box; }
  html, body { width: 1200px; height: 1000px; overflow: hidden; }
  body { background: var(--stage); font-family: "Work Sans", Arial, sans-serif; position: relative; }

  .card { position: absolute; left: 253px; width: 694px; height: 399px; border-radius: 20px; overflow: hidden; }

  .card-front { top: 73px; background: var(--card-dark); }
  .front-texture {
    position: absolute; inset: 0;
    background: linear-gradient(100deg, #151515 0%, var(--card-dark-edge) 45%, #2a2a2a 100%);
  }
  .front-brand {
    position: absolute; left: 520px; top: 272px;
    display: flex; align-items: center; gap: 8px;
    color: #ffffff; font-weight: 700; font-size: 15px; letter-spacing: 0.5px;
  }
  .brand-square { width: 14px; height: 14px; background: var(--brand-red); }

  .card-back { top: 519px; background: var(--card-light); }
  .back-decor {
    position: absolute; right: 0; top: 0; width: 310px; height: 399px;
    background: linear-gradient(160deg, var(--decor-cool) 0%, #ffffff 45%, var(--decor-warm) 100%);
    opacity: 0.8;
  }
  .back-brand {
    position: absolute; left: 0; right: 0; top: 62px;
    display: flex; justify-content: center; align-items: center; gap: 10px;
    color: var(--brand-red); font-weight: 700; font-size: 26px; letter-spacing: 0.5px; text-transform: uppercase;
  }
  .back-brand .brand-square { width: 22px; height: 22px; }

  .identity { position: absolute; right: 364px; top: 194px; text-align: right; }
  .identity-name { font-family: "Anton", Impact, sans-serif; font-size: 33px; line-height: 1; color: var(--ink); }
  .identity-role { margin-top: 6px; font-weight: 600; font-size: 14px; letter-spacing: 1.5px; color: var(--ink); }

  .divider { position: absolute; left: 347px; top: 175px; width: 2px; height: 90px; background: var(--brand-red); }

  .contacts { position: absolute; left: 365px; top: 179px; list-style: none; }
  .contacts li { display: flex; align-items: center; height: 28px; font-size: 19px; color: var(--ink-soft); }
  .contacts svg { width: 14px; height: 14px; margin-right: 13px; flex: none; }

  .address { position: absolute; left: 0; right: 0; top: 351px; text-align: center; font-size: 18px; color: var(--ink-soft); }
</style>
</head>
<body>
  <section class="card card-front">
    <div class="front-texture" role="img" aria-label="Dark embossed repeating brand pattern"></div>
    <div class="front-brand"><span class="brand-square"></span>Corvane Supplies</div>
  </section>

  <section class="card card-back">
    <div class="back-decor" role="img" aria-label="Faint outlined brand decoration"></div>
    <div class="back-brand"><span class="brand-square"></span>Corvane Supplies</div>

    <div class="identity">
      <div class="identity-name">Name Surname</div>
      <div class="identity-role">POSITION</div>
    </div>
    <div class="divider"></div>

    <ul class="contacts">
      <li>
        <svg viewBox="0 0 14 14"><rect x="3.5" y="0.8" width="7" height="12.4" rx="1.3" fill="none" stroke="var(--brand-cyan)" stroke-width="1.5"/><circle cx="7" cy="10.8" r="0.9" fill="var(--brand-cyan)"/></svg>
        (555)014-2870
      </li>
      <li>
        <svg viewBox="0 0 14 14"><rect x="0.5" y="2.5" width="13" height="9" fill="var(--brand-cyan)"/><path d="M0.8 3 L7 8 L13.2 3" fill="none" stroke="#ffffff" stroke-width="1.2"/></svg>
        sales@corvanesupplies.com
      </li>
      <li>
        <svg viewBox="0 0 14 14"><circle cx="7" cy="7" r="6" fill="none" stroke="var(--brand-cyan)" stroke-width="1.3"/><ellipse cx="7" cy="7" rx="2.6" ry="6" fill="none" stroke="var(--brand-cyan)" stroke-width="1"/><path d="M1 7 H13 M2 4 H12 M2 10 H12" stroke="var(--brand-cyan)" stroke-width="1"/></svg>
        corvanesupplies.com
      </li>
    </ul>

    <div class="address">412 N.Larkmoor Suite 5, Brenton, Tx 79700</div>
  </section>
</body>
</html>
```